Cartwell Design for Supplement Brand

We need a modern, sleek, and upscale Cartwell design for PureMeadow.com, built around our supplement bottles as the hero elements (not logo-heavy). NOTE: PLEASE DO NOT MAKE THIS DESIGN LOOK LIKE THE CURRENT DESIGN ON PUREMEADOW.COM AS WE DO NOT LIKE IT; YOU DON'T HAVE TO USE THOSE SAME COLORS OR LOGO THAT IS CURRENTLY THERE .
Please use or recommend a premium Cartwell theme (Cascade, Tapestry, Windcatcher, Copper, Tide, etc.) to minimize custom coding, while creating a stunning, conversion-focused storefront that feels more like a luxury wellness/beauty brand than a typical supplement site. Content and headlines can be adapted from our current supplements pages at https://www.rkmarlowonline.com/supplements/
And for any stock photography or images, focus on african-american and latina women

```html
<!DOCTYPE html>
<html lang="en">
<head>
<meta charset="utf-8">
<title>Pure Meadow – Storefront</title>
<link href="https://fonts.googleapis.com/css2?family=League+Spartan:wght@500;600&family=Poppins:wght@400;500&display=swap" rel="stylesheet">
<style>
:root{
  --board:#c6c6c6; --green:#6bbb6b; --green-dark:#55a555; --navy:#2f4f6c; --ink:#222;
  --hero:#effbe0; --mint:#f7fbea; --sky:#eef5fc; --white:#fff; --muted:#555; --line:#cfd8cf;
  --pink:#fbe2f0; --lilac:#e6e9fb; --teal:#dff0ea; --star:#f5c518;
}
*{margin:0;padding:0;box-sizing:border-box}
html,body{width:1200px;height:2420px;overflow:hidden;background:var(--board)}
body{font-family:"Poppins",sans-serif;color:var(--ink)}
.board{position:absolute;left:0;top:0;width:1277px;height:2576px;transform:scale(.9397);transform-origin:0 0;background:var(--board)}
.abs{position:absolute}
.head{font-family:"League Spartan",sans-serif;font-weight:600;color:var(--navy)}
.center{text-align:center}
.btn{position:absolute;background:var(--green);color:#fff;font-size:11px;display:flex;align-items:center;justify-content:center;letter-spacing:.3px}
.arrow{position:absolute;border:1.5px solid var(--navy);border-radius:50%;background:#fff;display:flex;align-items:center;justify-content:center;color:var(--navy);font-size:13px;font-weight:500}
.photo{position:absolute}
.desk{position:absolute;left:90px;top:78px;width:850px;height:2419px;background:#fff;overflow:hidden}
.topbar{position:absolute;left:0;top:0;width:850px;height:23px;background:var(--green);color:#fff;font-size:8px;display:flex;align-items:center;justify-content:center}
.lang{position:absolute;right:72px;top:6px;font-size:7px;color:#fff}
.nav-link{position:absolute;top:38px;font-size:9px;color:var(--ink)}
.logo{position:absolute;display:flex;align-items:center;gap:5px;font-family:"League Spartan",sans-serif;font-weight:600;color:var(--green-dark)}
.logo i{display:block;border-radius:50%;background:var(--green)}
.hero{position:absolute;left:0;top:60px;width:850px;height:469px;background:var(--hero)}
.card-img{position:absolute;top:679px;width:174px;height:160px;background:#f2fbf0}
.card-img .arch{position:absolute;left:30px;top:12px;width:112px;height:148px;border-radius:56px 56px 0 0}
.card-img .bottles{position:absolute;left:22px;top:60px;width:130px;height:76px;border-radius:6px;background:linear-gradient(180deg,#fafafa,#e8e8ee)}
.card-img .plus{position:absolute;right:12px;bottom:14px;width:16px;height:16px;border-radius:50%;background:#fff;font-size:10px;display:flex;align-items:center;justify-content:center;color:var(--navy)}
.card-name{position:absolute;top:850px;font-family:"League Spartan",sans-serif;font-weight:500;font-size:15px;color:var(--navy)}
.card-price{position:absolute;top:875px;font-size:10px}
.testi{position:absolute;top:1626px;width:291px;height:160px;background:#fff;box-shadow:0 2px 8px rgba(0,0,0,.07);padding:28px 20px 0}
.testi h4{font-weight:500;font-size:10px;color:var(--navy)}
.testi .stars{position:absolute;right:28px;top:32px;color:var(--star);font-size:7px;letter-spacing:1px}
.testi p{margin-top:12px;font-size:7.6px;line-height:14px;color:#444}
.who{position:absolute;left:20px;bottom:12px;display:flex;align-items:center;gap:8px;font-size:9px;color:var(--navy)}
.who i{display:block;width:28px;height:28px;border-radius:50%;background:#c9a58a}
.foot-h{position:absolute;top:2222px;font-family:"League Spartan",sans-serif;font-weight:500;font-size:17px;color:var(--navy)}
.foot-t{position:absolute;font-size:9px;line-height:15px;color:#333}
.soc{position:absolute;top:2327px;width:20px;height:20px;border:1px solid var(--navy);border-radius:2px}
.ic{position:absolute;left:520px;width:20px;height:20px;border:1px solid var(--line);border-radius:3px;display:flex;align-items:center;justify-content:center}
.pay{position:absolute;width:20px;height:12px;border-radius:2px}
.mob{position:absolute;left:998px;top:85px;width:193px;height:1428px;background:#fff;overflow:hidden}
.m-head{font-family:"League Spartan",sans-serif;font-weight:500;color:var(--navy);text-align:center;position:absolute;left:0;width:193px}
.m-arrow{position:absolute;width:12px;height:12px;border:1px solid var(--navy);border-radius:50%;font-size:6px;display:flex;align-items:center;justify-content:center;color:var(--navy)}
.m-acc{position:absolute;left:22px;font-size:8px;color:var(--navy);width:150px}
.m-acc b{position:absolute;right:0;color:var(--green);font-weight:500}
</style>
</head>
<body>
<div class="board">

<div class="desk">
  <div class="topbar">SAVE 10% BY TAKING OUR HEALTH QUIZ</div>
  <div class="lang">English ▾</div>
  <div class="logo" style="left:78px;top:36px;font-size:12px"><i style="width:14px;height:14px"></i>Pure Meadow</div>
  <span class="nav-link" style="left:262px">Home</span>
  <span class="nav-link" style="left:317px">Collections <span style="color:var(--green)">▾</span></span>
  <span class="nav-link" style="left:397px">Products</span>
  <span class="nav-link" style="left:466px">About Us</span>
  <span class="nav-link" style="left:534px">Contact Us</span>
  <svg class="abs" style="left:704px;top:37px" width="90" height="14" viewBox="0 0 90 14" fill="none" stroke="#222" stroke-width="1.2">
    <circle cx="6" cy="6" r="4.5"/><line x1="9.5" y1="9.5" x2="12.5" y2="12.5"/>
    <line x1="22" y1="2" x2="22" y2="12" stroke="#999"/>
    <path d="M30 2h2l2 7h7l1.5-5H33"/><circle cx="35" cy="12" r="1"/><circle cx="40" cy="12" r="1"/>
    <line x1="56" y1="2" x2="56" y2="12" stroke="#999"/>
    <circle cx="71" cy="7" r="5.5"/><circle cx="71" cy="5.5" r="2"/>
  </svg>

  <section class="hero">
    <h1 class="abs" style="left:108px;top:126px;font-family:'League Spartan',sans-serif;font-weight:600;font-size:33px;line-height:38px;color:#222">Your Journey to<br>Wellness Starts Here!</h1>
    <p class="abs" style="left:108px;top:218px;font-size:16px">Explore the World of Health</p>
    <div class="btn" style="left:108px;top:266px;width:104px;height:29px;font-size:11px">SHOP NOW</div>
    <div class="abs" style="left:114px;top:400px;font-size:9px;display:flex;align-items:center;gap:6px;color:var(--navy)">‹ <span style="width:10px;height:10px;border:1px solid var(--navy);border-radius:50%;background:var(--navy);box-shadow:inset 0 0 0 2px #fff"></span><span style="width:9px;height:9px;border:1px solid var(--navy);border-radius:50%"></span><span style="width:9px;height:9px;border:1px solid var(--navy);border-radius:50%"></span> ›</div>
    <svg class="abs" style="left:415px;top:45px" width="395" height="395"><circle cx="197" cy="197" r="196" fill="#e3f6d6"/><circle cx="197" cy="197" r="160" fill="#d7f1c9"/></svg>
    <div class="photo" role="img" aria-label="Three white supplement bottles: two cream tubes and a capsule jar" style="left:468px;top:62px;width:280px;height:340px;border-radius:10px;background:linear-gradient(180deg,#fafafa 0%,#f0f0f0 60%,#d9ece0 85%,#e9d1d4 100%)"></div>
  </section>

  <h2 class="head center abs" style="left:0;width:850px;top:582px;font-size:34px">Featured product collections</h2>
  <div class="card-img" style="left:52px"><div class="arch" style="background:var(--pink)"></div><div class="bottles" role="img" aria-label="Liver Lumen bottles"></div><span class="plus">+</span></div>
  <div class="card-img" style="left:246px"><div class="arch" style="background:var(--pink)"></div><div class="bottles" role="img" aria-label="Belly Lumen bottles"></div><span class="plus">+</span></div>
  <div class="card-img" style="left:438px"><div class="arch" style="background:var(--lilac)"></div><div class="bottles" role="img" aria-label="Glucose Lumen bottles"></div><span class="plus">+</span></div>
  <div class="card-img" style="left:633px"><div class="arch" style="background:var(--teal)"></div><div class="bottles" role="img" aria-label="Cycle Lumen bottles"></div><span class="plus">+</span></div>
  <span class="card-name" style="left:57px">Liver Lumen</span><span class="card-price" style="left:57px">$100.00</span>
  <span class="card-name" style="left:253px">Belly Lumen</span><span class="card-price" style="left:253px">$100.00</span>
  <span class="card-name" style="left:441px">Glucose Lumen</span><span class="card-price" style="left:441px">$100.00</span>
  <span class="card-name" style="left:638px">Cycle Lumen</span><span class="card-price" style="left:638px">$100.00</span>
  <div class="arrow" style="left:35px;top:743px;width:32px;height:32px">‹</div>
  <div class="arrow" style="left:786px;top:743px;width:32px;height:32px">›</div>
  <div class="btn" style="left:373px;top:929px;width:104px;height:28px">VIEW ALL</div>

  <h2 class="head center abs" style="left:0;width:850px;top:1050px;font-size:34px;letter-spacing:.5px">EXPLORE A WORLD OF HEALTH!</h2>
  <div class="photo" role="img" aria-label="Smiling woman holding a Liver Lumen bottle" style="left:49px;top:1138px;width:180px;height:242px;background:linear-gradient(160deg,#e8ddd2,#a88a76 60%,#6b5a50)"></div>
  <div class="photo" role="img" aria-label="Smiling woman holding a Glucose Lumen bottle" style="left:241px;top:1138px;width:180px;height:242px;background:linear-gradient(160deg,#eef0f2,#7a6a60 55%,#2f3e66)"></div>
  <div class="photo" role="img" aria-label="Woman in a grey top holding a Belly Lumen bottle" style="left:434px;top:1138px;width:180px;height:242px;background:linear-gradient(160deg,#d8c7b0,#9a7d68 50%,#6d6a6c)"></div>
  <div class="photo" role="img" aria-label="Laughing woman holding a Cycle Lumen bottle" style="left:626px;top:1138px;width:180px;height:242px;background:linear-gradient(160deg,#9aa6b3,#6a5146 50%,#8fb1cf)"></div>
  <div class="arrow" style="left:35px;top:1240px;width:32px;height:32px">‹</div>
  <div class="arrow" style="left:786px;top:1240px;width:32px;height:32px">›</div>
  <div class="btn" style="left:373px;top:1425px;width:104px;height:28px">VIEW ALL</div>

  <section class="abs" style="left:0;top:1507px;width:850px;height:372px;background:var(--mint)"></section>
  <h2 class="head center abs" style="left:0;width:850px;top:1544px;font-size:34px">Testimonials</h2>
  <div class="testi" style="left:118px"><h4>Liver Lumen</h4><span class="stars">★★★★★</span><p>This product is amazing. I have been taking it for 5 months and noticed more energy, clearer skin, reduced back fat, smaller waistline and flatter stomach. Love this product.</p><div class="who"><i></i>Dana</div></div>
  <div class="testi" style="left:441px"><h4>Liver Lumen</h4><span class="stars">★★★★★</span><p>This is by far THE BEST supplement I have taken in a long time! I'm down 10 pounds..my blood sugar went from 6.7 to 5.8 and I'm about to order my second bottle. And no more sugar cravings!</p><div class="who"><i style="background:#6b4a3a"></i>Maren</div></div>
  <div class="arrow" style="left:67px;top:1690px;width:32px;height:32px">‹</div>
  <div class="arrow" style="left:749px;top:1690px;width:32px;height:32px">›</div>

  <section class="abs" style="left:0;top:1879px;width:850px;height:300px;background:var(--sky)"></section>
  <h2 class="head center abs" style="left:0;width:850px;top:1952px;font-size:34px">Subscribe to Our Emails</h2>
  <p class="center abs" style="left:0;width:850px;top:2005px;font-size:9.5px">Lorem ipsum dolor sit amet, consectetur adipiscing elit, sed do eiusmod tempor</p>
  <div class="abs" style="left:221px;top:2064px;width:409px;height:46px;border:1px solid var(--navy);background:#fff;display:flex;align-items:center;justify-content:space-between;padding:0 26px 0 18px"><span style="font-size:8px;color:#666">Enter Your Email Address</span><span style="font-size:10px;color:var(--navy);font-weight:500">SUBSCRIBE</span></div>

  <h3 class="foot-h" style="left:115px">About</h3>
  <p class="foot-t" style="left:115px;top:2247px;width:150px">Lorem ipsum dolor sit amet, consectetur adipiscing elit, sed do eiusmod tempor incididunt ut labore et</p>
  <span class="soc" style="left:114px"></span><span class="soc" style="left:143px"></span><span class="soc" style="left:172px"></span><span class="soc" style="left:201px"></span>
  <h3 class="foot-h" style="left:337px">Quick Links</h3>
  <p class="foot-t" style="left:340px;top:2249px;line-height:19px"><span style="color:var(--green)">»</span> Home<br><span style="color:var(--green)">»</span> Collections<br><span style="color:var(--green)">»</span> Products<br><span style="color:var(--green)">»</span> About Us<br><span style="color:var(--green)">»</span> Contact Us</p>
  <h3 class="foot-h" style="left:518px">Contact Us</h3>
  <div class="ic" style="top:2256px"><svg width="10" height="10" viewBox="0 0 10 10"><path d="M2 1l2 2-1 1.5c.7 1.3 1.3 2 2.5 2.5L7 6l2 2-1.5 1.5C4.5 9 1 5.5.5 2.5z" fill="none" stroke="#6bbb6b" stroke-width=".9"/></svg></div>
  <p class="foot-t" style="left:554px;top:2252px;line-height:12px">CALL US<br>010 2040 555</p>
  <div class="ic" style="top:2292px"><svg width="10" height="8" viewBox="0 0 10 8"><rect x=".5" y=".5" width="9" height="7" fill="none" stroke="#6bbb6b"/><path d="M.5 .5L5 4.5 9.5.5" fill="none" stroke="#6bbb6b"/></svg></div>
  <p class="foot-t" style="left:554px;top:2288px;line-height:12px">EMAIL US<br>hello@puremeadow.com</p>
  <div class="ic" style="top:2329px"><svg width="8" height="11" viewBox="0 0 8 11"><path d="M4 10.5S.5 6.5.5 4a3.5 3.5 0 017 0c0 2.5-3.5 6.5-3.5 6.5z" fill="none" stroke="#6bbb6b"/><circle cx="4" cy="4" r="1.2" fill="#6bbb6b"/></svg></div>
  <p class="foot-t" style="left:554px;top:2323px;line-height:12px">Dummy Address Line,<br>Country Code</p>
  <div class="abs" style="left:49px;top:2369px;width:720px;height:1px;background:#bbb"></div>
  <div class="btn" style="left:773px;top:2354px;width:28px;height:27px;font-size:13px">↑</div>
  <p class="abs" style="left:60px;top:2390px;font-size:8px;color:#555">© 2025, Larkin - Health &amp; Beauty Storefront Theme Powered by Cartwell</p>
  <span class="pay" style="left:564px;top:2389px;background:#e3e6ee"></span><span class="pay" style="left:591px;top:2389px;background:#e3e6ee"></span><span class="pay" style="left:618px;top:2389px;background:#e3e6ee"></span><span class="pay" style="left:645px;top:2389px;background:#e3e6ee"></span><span class="pay" style="left:672px;top:2389px;background:#e3e6ee"></span><span class="pay" style="left:699px;top:2389px;background:#e3e6ee"></span>
</div>

<div class="mob">
  <div class="abs" style="left:0;top:0;width:193px;height:9px;background:var(--green);color:#fff;font-size:4px;text-align:center;line-height:9px">SAVE 10% BY TAKING OUR HEALTH QUIZ</div>
  <div class="abs" style="left:6px;top:13px;width:8px;height:5px;border-top:1px solid #333;border-bottom:1px solid #333"></div>
  <div class="logo" style="left:74px;top:12px;font-size:5px"><i style="width:6px;height:6px"></i>Pure Meadow</div>
  <div class="abs" style="left:158px;top:13px;display:flex;gap:3px"><span style="width:6px;height:6px;border:1px solid #333;border-radius:50%"></span><span style="width:6px;height:6px;border:1px solid #333"></span><span style="width:6px;height:6px;border:1px solid #333;border-radius:50%"></span></div>
  <section class="abs" style="left:0;top:27px;width:193px;height:271px;background:var(--hero)"></section>
  <div class="photo" role="img" aria-label="Three white supplement bottles" style="left:47px;top:30px;width:100px;height:120px;border-radius:6px;background:linear-gradient(180deg,#fafafa,#eee 70%,#e6cfd3)"></div>
  <h2 class="m-head" style="top:177px;font-size:15px;font-weight:600;color:#222;line-height:18px">Your Journey to<br>Wellness Starts Here!</h2>
  <p class="abs center" style="left:0;width:193px;top:221px;font-size:7px">Explore the World of Health</p>
  <div class="btn" style="left:71px;top:241px;width:51px;height:12px;font-size:4.5px">SHOP NOW</div>
  <div class="abs center" style="left:0;width:193px;top:265px;font-size:8px;color:var(--navy)">‹ ◉ ○ ○ ›</div>
  <h3 class="m-head" style="top:320px;font-size:12px;line-height:15px">Featured product<br>collections</h3>
  <div class="abs" style="left:20px;top:365px;width:154px;height:140px;background:#f2fbf0">
    <div class="abs" style="left:27px;top:11px;width:100px;height:129px;border-radius:50px 50px 0 0;background:var(--pink)"></div>
    <div class="abs" role="img" aria-label="Liver Lumen bottles" style="left:25px;top:55px;width:104px;height:58px;border-radius:5px;background:linear-gradient(180deg,#fafafa,#e8e8ee)"></div>
    <span class="abs" style="right:10px;bottom:12px;width:11px;height:11px;border-radius:50%;background:#fff;font-size:7px;text-align:center;line-height:11px">+</span>
  </div>
  <p class="m-head" style="top:516px;font-size:11px">Liver Lumen</p>
  <p class="abs center" style="left:0;width:193px;top:533px;font-size:8px">$100.00</p>
  <span class="m-arrow" style="left:81px;top:559px">‹</span><span class="m-arrow" style="left:99px;top:559px">›</span>
  <div class="btn" style="left:49px;top:586px;width:95px;height:25px;font-size:9px">VIEW ALL</div>
  <h3 class="m-head" style="top:654px;font-size:12px;line-height:15px">EXPLORE A WORLD<br>OF HEALTH!</h3>
  <div class="photo" role="img" aria-label="Woman in a grey top holding a Belly Lumen bottle" style="left:19px;top:703px;width:156px;height:180px;background:linear-gradient(160deg,#d8c7b0,#9a7d68 50%,#6d6a6c)"></div>
  <span class="m-arrow" style="left:81px;top:897px">‹</span><span class="m-arrow" style="left:99px;top:897px">›</span>
  <div class="btn" style="left:49px;top:926px;width:95px;height:25px;font-size:9px">VIEW ALL</div>
  <section class="abs" style="left:0;top:973px;width:193px;height:192px;background:var(--mint)"></section>
  <h3 class="m-head" style="top:992px;font-size:12px">Testimonials</h3>
  <div class="abs" style="left:18px;top:1028px;width:158px;height:100px;background:#fff;box-shadow:0 1px 5px rgba(0,0,0,.08);padding:15px 10px 0">
    <p style="font-size:5.5px;color:var(--navy)">Liver Lumen</p>
    <p style="font-size:4px;line-height:7px;color:#444;margin-top:5px">This product is amazing. I have been taking it for 5 months and noticed more energy, clearer skin, reduced back fat, smaller waistline and flatter stomach. Love this product.</p>
    <p style="color:var(--star);font-size:4px;margin-top:2px">★★★★★</p>
    <p style="display:flex;align-items:center;gap:4px;font-size:4.5px;margin-top:3px"><span style="width:14px;height:14px;border-radius:50%;background:#c9a58a"></span>Dana</p>
  </div>
  <span class="m-arrow" style="left:81px;top:1139px">‹</span><span class="m-arrow" style="left:99px;top:1139px">›</span>
  <section class="abs" style="left:0;top:1165px;width:193px;height:120px;background:var(--sky)"></section>
  <h3 class="m-head" style="top:1177px;font-size:12px;line-height:15px">Subscribe to<br>Our Emails</h3>
  <p class="abs center" style="left:30px;width:133px;top:1209px;font-size:4px;line-height:8px">Lorem ipsum dolor sit amet, consectetur adipi scing elit, sed do eiusmod tempor incididunt ut</p>
  <div class="abs" style="left:19px;top:1247px;width:155px;height:17px;border:1px solid var(--navy);background:#fff;display:flex;justify-content:space-between;align-items:center;padding:0 6px;font-size:3.6px"><span>Enter Your Email Address</span><span>SUBSCRIBE</span></div>
  <p class="m-acc" style="top:1300px">About Us<b>+</b></p>
  <p class="m-acc" style="top:1318px">Quick Links<b>+</b></p>
  <p class="m-acc" style="top:1336px">Contact Us<b>+</b></p>
  <div class="abs" style="left:6px;top:1356px;width:180px;height:1px;background:#ddd"></div>
  <span class="pay" style="left:24px;top:1371px;width:14px;height:8px;background:#e3e6ee"></span><span class="pay" style="left:48px;top:1371px;width:14px;height:8px;background:#e3e6ee"></span><span class="pay" style="left:73px;top:1371px;width:14px;height:8px;background:#e3e6ee"></span><span class="pay" style="left:98px;top:1371px;width:14px;height:8px;background:#e3e6ee"></span><span class="pay" style="left:123px;top:1371px;width:14px;height:8px;background:#e3e6ee"></span>
  <div class="btn" style="left:171px;top:1367px;width:15px;height:14px;font-size:7px">↑</div>
  <p class="abs center" style="left:0;width:193px;top:1390px;font-size:5.5px;line-height:7px;color:var(--navy)">© 2025,<br>Larkin - Health &amp; Beauty Storefront Theme<br>Powered by Cartwell</p>
</div>

</div>
</body>
</html>
```